website for MapleHarbor Partners - a HR Consultancy Company

Creation of a website template. I would like to make it with with Wix, but am open to other online website programms.

Website is for consulting company in human resources offering the following services:
- Human resources and talent management for small companies
- Human resources consulting for start-ups
- Diversity and Inclusion management/training
- Board of Directors - talent identification and need evalutation
- coaching and counseling

Pages needed:
- Home page
- HR and talent management
- HR consulting for start-ups
- Diversity & Inclusion management/training
- coaching and counseling
- contact

1. My logo below
2. an example website that I like (not in terms of colours): https://www.quillbrookadvisory.ch/
http://www.veltrimaxon.ch/

Target Market(s)

small and mid-sized companies, start-ups

Industry/Entity Type

Consulting

Number of Pages Required

5+ page

Font styles to use
Serif
Sans Serif

Colors
3277b5
35a7d7

Requirements
Must have
• - easy on the eye yet professional looking
• - my text is short
• - website should be clear and easy to understand
Nice to have
• - I will include photographs of the coaches
Should not have
• too many colours
• complicated

```html
<!DOCTYPE html>
<html lang="en">
<head>
<meta charset="utf-8">
<title>MapleHarbor Partners – Human Resources Coaching &amp; Consulting</title>
<link rel="stylesheet" href="https://fonts.googleapis.com/css2?family=Montserrat:wght@400;500;600&family=Open+Sans:wght@400;600&display=swap">
<style>
  :root {
    --brand-blue: #1b74bc;
    --panel-blue: rgba(30, 118, 192, 0.92);
    --ink: #2b2b2b;
    --body-text: #5c5c5c;
    --muted: #7a7a7a;
    --band-grey: #ededed;
    --bar-grey: #efefef;
    --rule: #d6d6d6;
    --white: #ffffff;
  }
  * { box-sizing: border-box; margin: 0; padding: 0; }
  html, body { width: 1200px; height: 2378px; overflow: hidden; background: var(--white); }
  body { position: relative; font-family: "Open Sans", Arial, sans-serif; color: var(--body-text); }

  /* Header */
  .site-header { position: absolute; left: 0; top: 0; width: 1200px; height: 135px; background: var(--white); }
  .brand { position: absolute; left: 116px; top: 30px; display: flex; align-items: center; gap: 12px; }
  .brand-dot { width: 34px; height: 34px; border-radius: 50%; background: var(--brand-blue); }
  .brand-name { font-family: "Montserrat", Arial, sans-serif; font-weight: 600; font-size: 23px; line-height: 1.15; color: var(--brand-blue); }
  .social { position: absolute; top: 27px; left: 923px; display: flex; gap: 4px; }
  .social span { width: 34px; height: 34px; border: 1.5px solid var(--brand-blue); border-radius: 50%; }
  .main-nav { position: absolute; top: 82px; left: 0; font-family: "Montserrat", Arial, sans-serif; font-size: 15px; color: #555; }
  .main-nav a { position: absolute; white-space: nowrap; color: inherit; text-decoration: none; letter-spacing: 0.3px; }
  .main-nav a.is-active { color: var(--brand-blue); }
  .main-nav a.is-active::after { content: ""; position: absolute; left: -5px; right: -5px; top: 47px; height: 4px; background: var(--brand-blue); }

  /* Hero */
  .hero { position: absolute; left: 0; top: 135px; width: 1200px; height: 540px;
    background: linear-gradient(90deg, #eef2f5 0%, #e3e9ee 35%, #c9d2da 60%, #b9c4ce 100%); }
  .hero-title { position: absolute; left: 117px; top: 195px; font-family: "Montserrat", Arial, sans-serif; font-weight: 500; font-size: 35px; line-height: 45px; letter-spacing: 1px; }
  .hero-title .line-accent { color: var(--brand-blue); display: block; }
  .hero-title .line-main { color: #151515; display: block; }
  .hero-dashes { position: absolute; left: 117px; top: 305px; display: flex; gap: 8px; }
  .hero-dashes span { width: 32px; height: 3px; background: #1a1a1a; }
  .hero-dashes span.is-current { background: var(--brand-blue); }

  /* Welcome */
  .welcome { position: absolute; left: 0; top: 675px; width: 1200px; height: 422px; text-align: center; border-bottom: 1px solid var(--rule); }
  .welcome h1 { margin-top: 78px; font-family: "Montserrat", Arial, sans-serif; font-weight: 500; font-size: 30px; color: var(--ink); letter-spacing: 0.5px; }
  .welcome h1 em { font-style: normal; color: var(--brand-blue); }
  .welcome p { width: 830px; margin: 0 auto; font-size: 14px; line-height: 25px; color: var(--body-text); }
  .welcome p.lead { margin-top: 22px; }
  .welcome p + p { margin-top: 12px; }
  .btn { display: inline-block; font-family: "Montserrat", Arial, sans-serif; font-weight: 600; font-size: 14px; letter-spacing: 0.5px; text-decoration: none; }
  .btn-outline-blue { position: absolute; left: 548px; top: 290px; width: 162px; height: 43px; line-height: 40px; border: 2px solid var(--brand-blue); color: var(--brand-blue); }

  /* Services */
  .services { position: absolute; left: 0; top: 1098px; width: 1200px; height: 427px; background: var(--band-grey); }
  .services h2 { position: absolute; top: 48px; width: 100%; text-align: center; font-family: "Montserrat", Arial, sans-serif; font-weight: 400; font-size: 28px; color: #333; letter-spacing: 0.5px; }
  .section-rule { position: absolute; left: 515px; top: 89px; width: 170px; height: 1px; background: #c4c4c4; }
  .section-rule::after { content: ""; position: absolute; left: 70px; top: -1px; width: 30px; height: 4px; background: #b0b0b0; }
  .service { position: absolute; top: 108px; width: 240px; text-align: center; }
  .service svg { display: block; margin: 0 auto; }
  .service p { margin-top: 18px; font-size: 16px; line-height: 25px; color: #444; }

  /* Why */
  .why { position: absolute; left: 0; top: 1525px; width: 1200px; height: 460px;
    background: linear-gradient(180deg, #cfe0ea 0%, #a9bfcc 45%, #7e97a6 70%, #5f6f75 100%); }
  .why-panel { position: absolute; left: 637px; top: 0; width: 441px; height: 460px; background: var(--panel-blue); color: var(--white); padding: 83px 56px 0 56px; }
  .why-panel h2 { font-family: "Montserrat", Arial, sans-serif; font-weight: 500; font-size: 27px; letter-spacing: 1px; }
  .why-panel p { margin-top: 16px; font-size: 14.5px; line-height: 25px; }
  .why-panel p + p { margin-top: 13px; }
  .btn-outline-white { margin-top: 28px; width: 155px; height: 41px; line-height: 38px; text-align: center; border: 1.5px solid var(--white); color: var(--white); font-size: 13.5px; }

  /* Footer */
  .site-footer { position: absolute; left: 0; top: 1985px; width: 1200px; height: 318px; background: var(--white); }
  .footer-col { position: absolute; top: 70px; }
  .footer-col h3 { font-family: "Montserrat", Arial, sans-serif; font-weight: 500; font-size: 19px; color: #111; }
  .footer-col ul { list-style: none; margin-top: 17px; }
  .footer-col li { font-size: 14px; line-height: 33.5px; color: var(--muted); }
  .footer-brand { position: absolute; left: 858px; top: 112px; display: flex; align-items: center; gap: 12px; }
  .footer-brand .brand-name { font-size: 24px; }

  .legal-bar { position: absolute; left: 0; top: 2303px; width: 1200px; height: 75px; background: var(--bar-grey); text-align: center; line-height: 72px; font-size: 13px; color: #888; }
</style>
</head>
<body>

<header class="site-header">
  <div class="brand">
    <span class="brand-dot"></span>
    <span class="brand-name">MapleHarbor<br>Partners</span>
  </div>
  <div class="social" aria-label="Social links"><span></span><span></span><span></span><span></span></div>
  <nav class="main-nav">
    <a class="is-active" style="left:437px">HOME</a>
    <a style="left:531px">ABOUT US</a>
    <a style="left:661px">SERVICES</a>
    <a style="left:783px">TEAM</a>
    <a style="left:873px">SOLUTION</a>
    <a style="left:1000px">CONTACT</a>
  </nav>
</header>

<section class="hero" role="img" aria-label="Photo of a smiling consultant holding papers in a bright office with colleagues and a laptop">
  <h1 class="hero-title">
    <span class="line-accent">HUMAN RESOURCES</span>
    <span class="line-main">COACHING &amp; CONSULTING</span>
  </h1>
  <div class="hero-dashes"><span></span><span></span><span class="is-current"></span><span></span></div>
</section>

<section class="welcome">
  <h1>WELCOME TO <em>MAPLEHARBOR</em></h1>
  <p class="lead">Fusce ultricies orci ac feugiat suscipit leo massa sodales velit et scelerisque mi tortor at ipsum cligula augue bibendum accumsan vestibulum ut commodo a mi Morbi ornare gravida elit Integer congue augue et malesuada iaculis ipsum dui aliquet felis at cursus magna nisl nec elit Praesent elementum elit at tellus nec</p>
  <p>ultricies sit amet porttitor mattis enim In massa libero interdum nec interdum vel blandit sed nulla In ullamcorper est eget tempor cursus neque mi consectetuer mi a ultricies massa est sed nisl Class aptent taciti sociosqu</p>
  <a class="btn btn-outline-blue">READ MORE</a>
</section>

<section class="services">
  <h2>OUR SERVICES</h2>
  <div class="section-rule"></div>

  <div class="service" style="left:94px">
    <svg width="130" height="140" viewBox="0 0 130 140" aria-hidden="true">
      <path d="M8 48 A62 62 0 0 1 122 48" fill="none" stroke="#777" stroke-width="7"/>
      <circle cx="65" cy="78" r="60" fill="var(--brand-blue)"/>
      <g fill="none" stroke="#fff" stroke-width="2.5" stroke-linecap="round">
        <path d="M48 104 V92 C38 86 38 66 50 58 C62 50 82 54 85 70 L90 80 L84 82 V92 H72 V104"/>
        <circle cx="64" cy="74" r="4"/>
        <ellipse cx="64" cy="74" rx="13" ry="5"/>
        <ellipse cx="64" cy="74" rx="13" ry="5" transform="rotate(60 64 74)"/>
        <ellipse cx="64" cy="74" rx="13" ry="5" transform="rotate(-60 64 74)"/>
      </g>
    </svg>
    <p>Human Resources and<br>talent management for<br>small companies</p>
  </div>

  <div class="service" style="left:343px">
    <svg width="130" height="140" viewBox="0 0 130 140" aria-hidden="true">
      <path d="M8 48 A62 62 0 0 1 122 48" fill="none" stroke="#777" stroke-width="7"/>
      <circle cx="65" cy="78" r="60" fill="var(--brand-blue)"/>
      <g fill="#fff">
        <circle cx="50" cy="62" r="5"/><circle cx="65" cy="58" r="5"/><circle cx="80" cy="62" r="5"/>
        <path d="M42 80 q8 -12 16 0z"/><path d="M57 76 q8 -12 16 0z"/><path d="M72 80 q8 -12 16 0z"/>
      </g>
      <g fill="none" stroke="#fff" stroke-width="2.5">
        <circle cx="50" cy="94" r="7"/><circle cx="80" cy="94" r="7"/><circle cx="65" cy="100" r="5"/>
      </g>
    </svg>
    <p>Human Resources<br>consulting for start-ups</p>
  </div>

  <div class="service" style="left:592px">
    <svg width="130" height="140" viewBox="0 0 130 140" aria-hidden="true">
      <path d="M8 48 A62 62 0 0 1 122 48" fill="none" stroke="#777" stroke-width="7"/>
      <circle cx="65" cy="78" r="60" fill="var(--brand-blue)"/>
      <g fill="none" stroke="#fff" stroke-width="2.5" stroke-linejoin="round">
        <rect x="42" y="56" width="46" height="46"/>
        <path d="M50 94 L78 66 M70 66 H78 V74"/>
        <path d="M58 88 L80 66"/>
      </g>
    </svg>
    <p>Diversity and Inclusion<br>management/training</p>
  </div>

  <div class="service" style="left:840px">
    <svg width="130" height="140" viewBox="0 0 130 140" aria-hidden="true">
      <path d="M8 48 A62 62 0 0 1 122 48" fill="none" stroke="#777" stroke-width="7"/>
      <circle cx="65" cy="78" r="60" fill="var(--brand-blue)"/>
      <g fill="none" stroke="#fff" stroke-width="2.5" stroke-linejoin="round">
        <rect x="52" y="52" width="16" height="12" rx="2"/>
        <rect x="64" y="58" width="16" height="12" rx="2"/>
      </g>
      <g fill="#fff">
        <circle cx="48" cy="76" r="5"/><circle cx="82" cy="76" r="5"/>
        <rect x="44" y="84" width="42" height="4"/>
        <rect x="62" y="88" width="6" height="14"/>
        <rect x="42" y="84" width="4" height="18"/><rect x="84" y="84" width="4" height="18"/>
      </g>
    </svg>
    <p>Coaching and<br>Counseling</p>
  </div>
</section>

<section class="why" role="img" aria-label="Photo of a red suspension bridge over a bay with a city skyline in the distance">
  <div class="why-panel">
    <h2>WHY WE ARE</h2>
    <p>Praesent elementum elit at tellus nec ultricies sit amet porttitor mattis enim In massa libero interdum nec interdum vel blandit</p>
    <p>sed nulla In ullamcorper est eget tempor cursus neque mi consectetuer mi a ultricies massa est sed nisl Class aptent taciti sociosqu ad litora</p>
    <a class="btn btn-outline-white">READ MORE</a>
  </div>
</section>

<footer class="site-footer">
  <div class="footer-col" style="left:149px">
    <h3>COMPANY</h3>
    <ul><li>Home</li><li>About Us</li><li>Mission</li><li>Why Us</li></ul>
  </div>
  <div class="footer-col" style="left:347px">
    <h3>SERVICES</h3>
    <ul><li>Talent management</li><li>Coaching and Counseling</li><li>Diversity and Inclusion management</li><li>Human Resources Consulting</li></ul>
  </div>
  <div class="footer-col" style="left:659px">
    <h3>RESOURCES</h3>
    <ul><li>Support</li><li>Team</li><li>Clients</li><li>Contact Us</li></ul>
  </div>
  <div class="footer-brand">
    <span class="brand-dot"></span>
    <span class="brand-name">MapleHarbor<br>Partners</span>
  </div>
</footer>

<div class="legal-bar">© 2017 Company Name&nbsp; All right reserved&nbsp; Term of Use</div>

</body>
</html>
```